Signage for a store*

logo on the two sides of the sign
in the middle is the name of the store witch is KORVELO
at the bottom of the two logos, one side for location/address and the other side is contact details phone number is 718-392-6170 address is 7342 THE SIGN WILL BEE 15 FEET BY 4 FEET I WOULD LIKE THAT THE
BACKGROUND OF THE SIGN SHOULD HAVE A NICE COLOR BASE
THAT GOES FOR A WINE STORE

```html
<!DOCTYPE html>
<html lang="en">
<head>
<meta charset="utf-8">
<title>KORVELO Wine Store – Sign</title>
<link rel="stylesheet" href="https://fonts.googleapis.com/css2?family=Rokkitt:wght@300;400&family=Playfair+Display:wght@700&family=Roboto+Condensed:wght@300&display=swap">
<style>
  :root {
    --canvas: #ffffff;
    --wine: #a51f40;
    --wine-light: #b8485f;
    --gold: #b8891f;
    --blush: #e6b39c;
    --numeral: #ebb9a8;
  }
  * { margin: 0; padding: 0; box-sizing: border-box; }
  html, body {
    width: 1200px;
    height: 1200px;
    overflow: hidden;
    background: var(--canvas);
  }
  .sign {
    position: absolute;
    left: 86px;
    top: 463px;
    width: 1028px;
    height: 274px;
    background: var(--wine);
    overflow: hidden;
  }
  .sign__sheen {
    position: absolute;
    inset: 0;
    background: linear-gradient(120deg, transparent 0 58%, rgba(255,255,255,0.12) 58% 100%);
    pointer-events: none;
  }
  .sign__pattern {
    position: absolute;
    inset: 0;
    background: radial-gradient(ellipse at 50% 50%, rgba(140,20,50,0.35), rgba(140,20,50,0) 70%);
  }
  .emblem {
    position: absolute;
    top: 30px;
    width: 150px;
    height: 182px;
    display: flex;
    flex-direction: column;
    align-items: center;
    justify-content: center;
    gap: 14px;
  }
  .emblem--left { left: 35px; }
  .emblem--right { left: 843px; }
  .emblem__mark {
    width: 64px;
    height: 64px;
    border: 2px solid var(--gold);
    border-radius: 50%;
  }
  .emblem__name {
    font-family: "Rokkitt", serif;
    font-weight: 300;
    font-size: 29px;
    line-height: 1;
    color: var(--gold);
    letter-spacing: 0.5px;
  }
  .store-name {
    position: absolute;
    left: 200px;
    width: 628px;
    top: 66px;
    text-align: center;
    font-family: "Rokkitt", serif;
    font-weight: 300;
    font-size: 126px;
    line-height: 1;
    color: var(--gold);
    letter-spacing: 1px;
  }
  .store-type {
    position: absolute;
    left: 200px;
    width: 628px;
    top: 209px;
    text-align: center;
    font-family: "Playfair Display", serif;
    font-weight: 700;
    font-size: 29px;
    line-height: 1;
    color: var(--blush);
    letter-spacing: 11px;
  }
  .footnote {
    position: absolute;
    top: 221px;
    width: 200px;
    text-align: center;
    font-family: "Roboto Condensed", sans-serif;
    font-weight: 300;
    font-size: 25px;
    line-height: 1;
    color: var(--numeral);
  }
  .footnote--address { left: 10px; }
  .footnote--phone { left: 818px; }
</style>
</head>
<body>
  <main class="sign">
    <div class="sign__pattern" role="img" aria-label="Faint tone-on-tone vine and leaf pattern across the sign background"></div>
    <div class="sign__sheen"></div>

    <div class="emblem emblem--left">
      <span class="emblem__mark"></span>
      <span class="emblem__name">KORVELO</span>
    </div>

    <h1 class="store-name">KORVELO</h1>
    <p class="store-type">WINE STORE</p>

    <div class="emblem emblem--right">
      <span class="emblem__mark"></span>
      <span class="emblem__name">KORVELO</span>
    </div>

    <p class="footnote footnote--address">– 7342 –</p>
    <p class="footnote footnote--phone">718-392-6170</p>
  </main>
</body>
</html>
```